Webpage for a treatment housing for young addicts.

I need a new design and files for my wordpress page. I need it to be more neat and clean. I need it to look professional with a starting page that will work as a navigation. I need like logo and phone number and such up top, a picture under it with one sentence as a slogan and under it 6 boxes to click to come to our different pages. Under it I want news etc.

Target Market(s)

Social services, employees and governements

Coding

Coded - Design and coding required

Font styles to use
Sans Serif

Colors
abd037
3176b5
9d9d9d
aaaaaa
f04a50

Requirements
Must have
• A nice design
Nice to have
• need it to look professional with a starting page that will work as a navigation. I need like logo and phone number and such up top, a picture under it with one sentence as a slogan and under it 6 boxes to click to come to our different pages. Under it I want news etc.
• today www.kelmora.se
• want more like www.trivest.se or www.solbrink.se
Should not have
• To many different colours and a messy design.

```html
<!DOCTYPE html>
<html lang="en">
<head>
<meta charset="utf-8">
<title>Kelmora – Care and Housing</title>
<link href="https://fonts.googleapis.com/css2?family=Montserrat:wght@400;500;600;700;800&family=Arimo:wght@400;700&display=swap" rel="stylesheet">
<style>
:root{
  --blue:#3176b5;
  --green:#abd037;
  --ink:#111111;
  --text:#222222;
  --muted:#9d9d9d;
  --soft:#f4f4f4;
  --white:#ffffff;
}
*{box-sizing:border-box;margin:0;padding:0}
html,body{width:1200px;height:3963px;overflow:hidden}
body{font-family:"Montserrat",sans-serif;color:var(--text);background:var(--white);position:relative}
a{color:inherit;text-decoration:none}
.abs{position:absolute}

/* top bar */
.topbar{position:absolute;left:0;top:0;width:1200px;height:42px;background:var(--blue);color:var(--white);font-size:15px}
.topbar .item{position:absolute;top:11px;display:flex;align-items:center;gap:9px}
.topbar svg{width:20px;height:20px}
.topbar .social{position:absolute;right:89px;top:11px;display:flex;gap:7px}
.topbar .social span{width:20px;height:20px;background:var(--white);border-radius:3px;display:block}

/* header */
.header{position:absolute;left:0;top:42px;width:1200px;height:135px;background:var(--white)}
.brand{position:absolute;left:91px;top:42px;display:flex;align-items:center;gap:12px}
.brand .mark{width:34px;height:34px;background:var(--green)}
.brand .name{font-weight:800;font-size:40px;color:var(--blue);letter-spacing:-0.5px}
.nav{position:absolute;right:92px;top:58px;display:flex;gap:31px;font-weight:600;font-size:16px;color:var(--ink)}
.nav .active{color:var(--green)}

/* hero */
.hero{position:absolute;left:0;top:177px;width:1200px;height:581px;background:linear-gradient(100deg,#4a4a4a 0%,#5d5650 45%,#7a6a58 62%,#3a3533 100%)}
.hero h1{position:absolute;left:87px;top:152px;font-weight:500;font-size:51px;line-height:60px;color:var(--white)}
.hero p{position:absolute;left:90px;top:295px;font-family:"Arimo",sans-serif;font-size:15px;color:var(--white)}
.btn-hero{position:absolute;left:89px;top:351px;width:177px;height:61px;border-radius:31px;background:var(--green);color:var(--white);font-size:21px;font-weight:500;display:flex;align-items:center;justify-content:center}

/* services */
.section-title{position:absolute;left:0;width:1200px;text-align:center;font-weight:800;font-size:35px;color:var(--ink)}
.card{position:absolute;width:305px;height:418px;background:var(--white);box-shadow:0 2px 10px rgba(0,0,0,.18);border-radius:4px;text-align:center}
.card .icon{position:absolute;left:102px;top:48px;width:102px;height:102px}
.card h3{position:absolute;left:0;right:0;top:207px;font-size:21px;font-weight:700;color:var(--ink)}
.card p{position:absolute;left:28px;right:28px;top:250px;font-size:16px;line-height:21px;color:var(--ink)}
.card .btn{position:absolute;left:86px;top:338px;width:133px;height:45px;border-radius:23px;background:var(--green);color:var(--ink);font-size:15px;display:flex;align-items:center;justify-content:center}
.card.featured{background:var(--blue)}
.card.featured h3,.card.featured p{color:var(--white)}
.card.featured .btn{background:var(--white)}
.card .icon svg{width:100%;height:100%;fill:none;stroke:var(--ink);stroke-width:3;stroke-linejoin:round;stroke-linecap:round}
.card.featured .icon svg{stroke:var(--white)}

/* about */
.about{position:absolute;left:0;top:1895px;width:1200px;height:480px;background:linear-gradient(90deg,#4a7eb0 0%,#3f78b4 55%,#356fae 100%);color:var(--white);text-align:center}
.about h2{position:absolute;left:0;right:0;top:70px;font-size:35px;font-weight:800}
.about p{position:absolute;left:100px;right:100px;top:162px;font-family:"Arimo",sans-serif;font-size:21px;line-height:43px}
.about .btn{position:absolute;left:523px;top:372px;width:148px;height:49px;border-radius:25px;background:var(--white);color:var(--ink);font-size:17px;display:flex;align-items:center;justify-content:center}

/* blogs */
.blogs{position:absolute;left:0;top:2375px;width:1200px;height:818px;background:var(--soft)}
.blogs .eyebrow{position:absolute;left:0;right:0;top:80px;text-align:center;font-size:16px;font-weight:700;color:var(--blue)}
.blogs h2{position:absolute;left:0;right:0;top:113px;text-align:center;font-size:35px;font-weight:800;color:var(--ink)}
.blogs .label{position:absolute;top:220px;font-family:"Arimo",sans-serif;font-size:17px;color:var(--ink)}
.photo{position:absolute}
.date{position:absolute;background:var(--blue);color:var(--white);font-size:14px;font-weight:500}
.feature-title{position:absolute;left:107px;top:528px;font-size:28px;font-weight:700;color:var(--ink)}
.feature-text{position:absolute;left:107px;top:568px;width:450px;font-family:"Arimo",sans-serif;font-size:16px;line-height:21.5px;color:var(--ink)}
.readmore{position:absolute;font-family:"Arimo",sans-serif;font-weight:700;font-size:16px;color:var(--blue)}
.comments{position:absolute;font-family:"Arimo",sans-serif;font-size:13px;color:var(--blue)}
.post-title{position:absolute;left:858px;width:260px;font-size:18px;font-weight:700;line-height:21px;color:var(--ink)}
.post-text{position:absolute;left:859px;width:260px;font-family:"Arimo",sans-serif;font-size:15px;line-height:21.5px;color:var(--ink)}

/* newsletter */
.newsletter{position:absolute;left:0;top:3193px;width:1200px;height:293px;background:var(--blue);color:var(--white)}
.newsletter h2{position:absolute;left:160px;width:240px;top:96px;text-align:center;font-size:28px;font-weight:800;line-height:35px}
.newsletter .divider{position:absolute;left:413px;top:50px;width:4px;height:175px;background:#e6e6e6}
.newsletter p{position:absolute;left:469px;top:94px;font-family:"Arimo",sans-serif;font-size:16px}
.subscribe{position:absolute;left:449px;top:140px;width:591px;height:53px;background:var(--white);border-radius:27px}
.subscribe .field{position:absolute;left:18px;top:16px;font-size:17px;color:var(--ink)}
.subscribe .go{position:absolute;right:0;top:0;width:199px;height:53px;background:var(--ink);border-radius:27px;color:var(--white);font-size:22px;font-weight:500;display:flex;align-items:center;justify-content:center}

/* footer */
.footer{position:absolute;left:0;top:3486px;width:1200px;height:477px;background:var(--white)}
.footer .brand{left:105px;top:200px}
.footer .brand .mark{width:48px;height:48px}
.footer .brand .name{font-size:56px}
.footer h4{position:absolute;top:124px;font-size:18px;font-weight:700;color:var(--ink)}
.footer ul{position:absolute;top:166px;list-style:none;font-family:"Arimo",sans-serif;font-size:15px;line-height:27px;color:var(--ink)}
.footer .social{position:absolute;left:934px;top:170px;display:flex;gap:9px}
.footer .social span{width:20px;height:20px;background:var(--ink);border-radius:3px;display:block}
.copyright{position:absolute;left:0;right:0;top:421px;text-align:center;font-family:"Arimo",sans-serif;font-size:16px;color:var(--ink)}
</style>
</head>
<body>

<div class="topbar">
  <div class="item" style="left:110px">
    <svg viewBox="0 0 20 20" fill="none" stroke="#fff" stroke-width="1.4"><circle cx="10" cy="10" r="8"/><path d="M10 5v5l3 2"/></svg>
    <span>Monday - Friday 9:00 - 18:00</span>
  </div>
  <div class="item" style="left:398px">
    <svg viewBox="0 0 20 20" fill="none" stroke="#fff" stroke-width="1.4"><rect x="2" y="4" width="16" height="12"/><path d="M2 4l8 7 8-7"/></svg>
    <span>info@kelmora.se</span>
  </div>
  <div class="item" style="left:564px">
    <svg viewBox="0 0 20 20" fill="#fff"><path d="M5 2l3 4-2 2c1 2 3 4 5 5l2-2 4 3-2 3C9 17 3 11 2 5z"/></svg>
    <span>010-4417820</span>
  </div>
  <div class="social"><span></span><span></span><span></span><span></span><span></span></div>
</div>

<header class="header">
  <a class="brand" href="#"><span class="mark"></span><span class="name">Kelmora</span></a>
  <nav class="nav">
    <a class="active" href="#">Home</a>
    <a href="#">About Kelmora</a>
    <a href="#">Lindgården Hvb</a>
    <a href="#">Work With Us</a>
    <a href="#">Plug</a>
  </nav>
</header>

<section class="hero" role="img" aria-label="Photo of a young woman talking with a counsellor in a warm living room">
  <h1>"We Create Sustainable<br>Roads to a Better Future"</h1>
  <p>Kelmora Sverige AB carries out care and care aimed at people aged 14-25 years.</p>
  <a class="btn-hero" href="#">More view</a>
</section>

<h2 class="section-title" style="top:818px">WHAT WE DO</h2>

<div class="card" style="left:100px;top:926px">
  <div class="icon"><svg viewBox="0 0 100 100"><circle cx="50" cy="30" r="10"/><path d="M34 62c0-12 7-18 16-18s16 6 16 18"/><path d="M10 40l4 28 18 20M90 40l-4 28-18 20"/></svg></div>
  <h3>Personal assistance</h3>
  <p>Lorem Ipsum is simply dummy text of the printing and typesetting industry.</p>
  <a class="btn" href="#">Read More</a>
</div>
<div class="card featured" style="left:443px;top:926px">
  <div class="icon"><svg viewBox="0 0 100 100"><path d="M82 10l10 10-44 44-10-10z"/><path d="M38 54L14 78l-4 14 14-4 24-24"/><path d="M72 20l10 10"/></svg></div>
  <h3>Therapies</h3>
  <p>Lorem Ipsum is simply dummy text of the printing and typesetting industry.</p>
  <a class="btn" href="#">Read More</a>
</div>
<div class="card" style="left:789px;top:926px">
  <div class="icon"><svg viewBox="0 0 100 100"><circle cx="50" cy="26" r="12"/><rect x="32" y="44" width="36" height="44" rx="6"/><circle cx="14" cy="18" r="10"/><circle cx="86" cy="18" r="10"/><circle cx="14" cy="82" r="10"/><circle cx="86" cy="82" r="10"/></svg></div>
  <h3>Individual</h3>
  <p>Lorem Ipsum is simply dummy text of the printing and typesetting industry.</p>
  <a class="btn" href="#">Read More</a>
</div>

<div class="card" style="left:101px;top:1397px">
  <div class="icon"><svg viewBox="0 0 100 100"><path d="M20 14h74v54H20z"/><path d="M6 28h66v50H30l-14 14V78H6z"/><path d="M32 44h12V32h12v12h12v12H56v12H44V56H32z"/></svg></div>
  <h3>About Kelmora</h3>
  <p>Lorem Ipsum is simply dummy text of the printing and typesetting industry.</p>
  <a class="btn" href="#">Read More</a>
</div>
<div class="card" style="left:443px;top:1397px">
  <div class="icon"><svg viewBox="0 0 100 100"><path d="M40 40l30-26 28 26v46H40z"/><path d="M54 52h32v20H54z"/><circle cx="26" cy="72" r="16"/><circle cx="26" cy="34" r="7"/></svg></div>
  <h3>Disability</h3>
  <p>Lorem Ipsum is simply dummy text of the printing and typesetting industry.</p>
  <a class="btn" href="#">Read More</a>
</div>
<div class="card" style="left:789px;top:1397px">
  <div class="icon"><svg viewBox="0 0 100 100"><path d="M30 92V30h40v62M8 92V50h22M70 50h22v42M4 92h92"/><path d="M50 30V6h12v8H50"/><rect x="40" y="40" width="8" height="10"/><rect x="52" y="40" width="8" height="10"/><rect x="44" y="72" width="12" height="20"/></svg></div>
  <h3>School</h3>
  <p>Lorem Ipsum is simply dummy text of the printing and typesetting industry.</p>
  <a class="btn" href="#">Read More</a>
</div>

<section class="about" role="img" aria-label="Blue-toned photo of a man in a suit standing in a bright office">
  <h2>ABOUT US</h2>
  <p>We at Kelmora believe individuals possess incredible knowledge and opportunities to create incredibly good situations. Mostly more than you may think. This applies to all clients as employees.<br>We therefore want to create opportunities for everyone to make use of their true skills.</p>
  <a class="btn" href="#">Read More</a>
</section>

<section class="blogs">
  <div class="eyebrow">INSIGHTS</div>
  <h2>EXPLORE OUR BLOGS</h2>
  <div class="label" style="left:88px">MOST POPULAR BLOGS</div>
  <div class="label" style="left:615px">LATEST BLOGS</div>

  <div class="photo" style="left:89px;top:280px;width:496px;height:231px;background:linear-gradient(180deg,#dfe6e8 0%,#b9c3a4 40%,#7c3a34 62%,#6f8a5a 100%)" role="img" aria-label="Photo of red wooden houses on a green lawn"></div>
  <div class="date" style="left:92px;top:487px;width:124px;height:24px;text-align:center;line-height:24px">22 DEC 2018</div>
  <div class="feature-title">Standard Lorem Ipsum passage</div>
  <div class="feature-text">Lorem ipsum dolor sit amet, consectetur adipiscing elit, sed do eiusmod tempor incididunt ut labore et dolore magna aliqua. Ut enim ad minim veniam, quis nostrud exercitation ullamco laboris nisi ut aliquip ex ea commodo consequat.</div>
  <a class="readmore" style="left:107px;top:2709px;top:709px" href="#">READ MORE</a>
  <div class="comments" style="left:443px;top:711px">22 Comments</div>

  <div class="photo" style="left:615px;top:280px;width:226px;height:218px;background:linear-gradient(180deg,#ddd5c8 0%,#a99680 30%,#7c2f2c 55%,#c9b59a 100%)" role="img" aria-label="Photo of a red house facade with white windows"></div>
  <div class="date" style="left:615px;top:280px;width:54px;height:52px;padding:6px 5px;line-height:19px">22 DEC 2018</div>
  <div class="post-title" style="top:291px">Standard Lorem Ipsum passage</div>
  <div class="post-text" style="top:377px">Lorem ipsum dolor sit amet, consectetur adipiscing elit, sed do eiusmod tempor incididunt ut</div>
  <a class="readmore" style="left:862px;top:484px" href="#">READ MORE</a>
  <div class="comments" style="left:1020px;top:485px">15 Comments</div>

  <div class="photo" style="left:615px;top:517px;width:226px;height:218px;background:linear-gradient(180deg,#c8c2b6 0%,#9a5a46 40%,#8a4a3c 70%,#8a8a5a 100%)" role="img" aria-label="Photo of an old brick house with white windows"></div>
  <div class="date" style="left:615px;top:517px;width:54px;height:52px;padding:6px 5px;line-height:19px">22 DEC 2018</div>
  <div class="post-title" style="top:527px">Standard Lorem Ipsum passage</div>
  <div class="post-text" style="top:600px">Lorem ipsum dolor sit amet, consectetur adipiscing elit, sed do eiusmod tempor incididunt ut</div>
  <a class="readmore" style="left:861px;top:709px" href="#">READ MORE</a>
  <div class="comments" style="left:1020px;top:710px">15 Comments</div>
</section>

<section class="newsletter">
  <h2>NEWSLETTER SIGN UP</h2>
  <div class="divider"></div>
  <p>Subscribe to our newsletter to get the Kelmora Sverige AB right to your inbox</p>
  <div class="subscribe">
    <span class="field">Enter the email</span>
    <span class="go">Subscribe</span>
  </div>
</section>

<footer class="footer">
  <a class="brand" href="#"><span class="mark"></span><span class="name">Kelmora</span></a>
  <h4 style="left:528px">QUICK LINKS</h4>
  <ul style="left:528px"><li>Home</li><li>About Kelmora</li><li>Lindgården Hvb</li><li>Work With Us</li><li>&nbsp;Plug</li></ul>
  <h4 style="left:737px">SERVICES</h4>
  <ul style="left:737px"><li>Personal assistance</li><li>Individual</li><li>About Kelmora</li><li>Disability</li><li>School</li><li>Therapies</li></ul>
  <h4 style="left:933px">SOCIAL NETWORK</h4>
  <div class="social"><span></span><span></span><span></span><span></span><span></span></div>
  <div class="copyright">© Copyright Reserved Kelmora</div>
</footer>

</body>
</html>
```